Iron and home washing service

I provide I home iron and washing service for adult and kids clothes on a smoke pet free environment. I can collect and offer a next day delivery. Or same day depend on items and volume. I offer competitive frendly and reliable service and price. I charge by weight £4,50 / kg. approx 5 items =1 kg minimum for collection.

```html
<!DOCTYPE html>
<html lang="en">
<head>
<meta charset="utf-8">
<title>Iron and Home Washing Service</title>
<link rel="stylesheet" href="https://fonts.googleapis.com/css2?family=Michroma&family=Roboto:wght@400;500;700&display=swap">
<style>
  :root {
    --charcoal-deep: #1c1c1e;
    --charcoal: #3a3a3d;
    --charcoal-light: #555558;
    --orange: #e8531f;
    --orange-bright: #f06a24;
    --red: #c9251d;
    --yellow: #ffe81a;
    --white: #ffffff;
    --ink: #3b3b3b;
    --photo-light: #f4f6f9;
    --photo-blue: #7fb4e3;
    --page: #d9d9d9;
  }
  html, body {
    margin: 0;
    padding: 0;
    width: 1200px;
    height: 873px;
    overflow: hidden;
    background: var(--page);
  }
  .flyer {
    position: relative;
    width: 1200px;
    height: 873px;
    overflow: hidden;
    font-family: "Roboto", Arial, sans-serif;
  }
  .flyer-shapes {
    position: absolute;
    inset: 0;
  }
  .flyer-text {
    position: absolute;
    margin: 0;
    white-space: nowrap;
  }
  .eyebrow {
    left: 0;
    width: 600px;
    top: 62px;
    display: flex;
    justify-content: center;
    align-items: center;
    gap: 18px;
    font-family: "Michroma", "Arial Black", sans-serif;
    font-size: 34px;
    letter-spacing: 6px;
    color: var(--white);
  }
  .eyebrow::before,
  .eyebrow::after {
    content: "";
    width: 90px;
    height: 2px;
    background: var(--white);
  }
  .headline {
    left: 0;
    width: 600px;
    top: 116px;
    text-align: center;
    font-weight: 700;
    font-size: 46px;
    color: var(--yellow);
  }
  .audience {
    left: 44px;
    top: 226px;
    line-height: 1.2;
  }
  .audience-line {
    display: block;
    font-weight: 500;
    font-size: 30px;
    color: var(--ink);
    color: var(--charcoal-deep);
  }
  .audience-highlight {
    display: block;
    font-size: 38px;
    color: var(--yellow);
  }
  .delivery {
    left: 0;
    width: 663px;
    top: 452px;
    text-align: center;
  }
  .delivery-title {
    display: block;
    font-family: "Michroma", "Arial Black", sans-serif;
    font-size: 24px;
    letter-spacing: 3px;
    color: var(--yellow);
    text-decoration: underline;
    text-underline-offset: 5px;
    text-decoration-thickness: 2px;
  }
  .delivery-detail {
    display: block;
    margin-top: 24px;
    font-size: 21px;
    line-height: 1.4;
    color: var(--charcoal-deep);
    white-space: normal;
  }
  .pricing {
    left: 46px;
    top: 640px;
    font-family: "Michroma", "Arial Black", sans-serif;
    font-size: 21px;
    letter-spacing: 4px;
    line-height: 39px;
    color: var(--white);
  }
  .call {
    left: 44px;
    top: 808px;
    font-size: 30px;
    color: var(--yellow);
  }
  .call-number {
    font-weight: 700;
    font-size: 36px;
    color: var(--white);
    margin-left: 6px;
  }
  .website {
    left: 782px;
    top: 62px;
    font-weight: 500;
    font-size: 30px;
    color: var(--ink);
  }
</style>
</head>
<body>
<main class="flyer">
  <svg class="flyer-shapes" width="1200" height="873" viewBox="0 0 1200 873" aria-hidden="true">
    <defs>
      <linearGradient id="panel-sheen" x1="0" y1="0" x2="1" y2="1">
        <stop offset="0" stop-color="var(--charcoal-deep)"/>
        <stop offset="0.35" stop-color="var(--charcoal-light)"/>
        <stop offset="0.6" stop-color="var(--charcoal)"/>
        <stop offset="1" stop-color="var(--charcoal-deep)"/>
      </linearGradient>
      <linearGradient id="band-orange" x1="0" y1="0" x2="1" y2="0">
        <stop offset="0" stop-color="var(--orange)"/>
        <stop offset="1" stop-color="var(--orange-bright)"/>
      </linearGradient>
      <linearGradient id="photo-tone" x1="0" y1="0" x2="0.6" y2="1">
        <stop offset="0" stop-color="var(--photo-light)"/>
        <stop offset="0.55" stop-color="#dfe6ee"/>
        <stop offset="1" stop-color="var(--photo-blue)"/>
      </linearGradient>
    </defs>
    <rect class="panel" x="0" y="0" width="1200" height="873" fill="url(#panel-sheen)"/>
    <rect class="band-audience" x="0" y="212" width="820" height="106" fill="url(#band-orange)"/>
    <polygon class="ribbon-red" points="0,332 780,424 0,424" fill="var(--red)"/>
    <rect class="band-delivery" x="0" y="428" width="663" height="169" fill="url(#band-orange)"/>
    <rect class="band-call" x="0" y="792" width="720" height="81" fill="var(--orange)"/>
    <path class="curve-band" d="M575,0 L640,0 Q970,436 655,873 L600,873 Q920,436 575,0 Z" fill="var(--orange)"/>
  </svg>

  <svg class="flyer-shapes" width="1200" height="873" viewBox="0 0 1200 873" role="img" aria-label="Photo of a blue steam iron beside a wicker laundry basket of folded clothes">
    <path class="photo-area" d="M640,0 H1200 V873 H655 Q970,436 640,0 Z" fill="url(#photo-tone)"/>
    <path class="photo-edge" d="M640,0 Q970,436 655,873" fill="none" stroke="var(--yellow)" stroke-width="9"/>
  </svg>

  <h1 class="flyer-text eyebrow">IRON AND</h1>
  <h2 class="flyer-text headline">HOME WASHING SERVICE</h2>

  <p class="flyer-text audience">
    <span class="audience-line">FOR ADULT AND KIDS CLOTHES ON A</span>
    <span class="audience-line audience-highlight">SMOKE PET FREE ENVIRONMENT</span>
  </p>

  <p class="flyer-text delivery">
    <span class="delivery-title">I CAN COLLECT AND OFFER</span>
    <span class="delivery-detail">A NEXT DAY DELIVERY OR SAME DAY DEPEND ON<br>ITEMS AND VOLUME</span>
  </p>

  <p class="flyer-text pricing">
    I CHARGE BY WEIGHT £4,50 / KG.<br>
    APPROX 5 ITEMS =1 KG MINIMUM<br>
    FOR COLLECTION.
  </p>

  <p class="flyer-text call">CALL US TODAY:<span class="call-number">XXX-XXX-XXXX</span></p>

  <p class="flyer-text website">www.yourwebsite.com</p>
</main>
</body>
</html>
```